Crew Maple Downgraders and Upgraders Leaflets part 2

Would like to create two double-sided dl card leaflets. This is for an Australian real estate company.

1. Will be to target older people in our area. The down sizers. What do they say when we speak to them – the yard is getting too big, we cant look after the gardens any more. So idea is

Headings could be;
Is Time You Gave Your Mower A Rest?
Give your Mower A Rest
Time To Sell The Lawn Mower?

Call Crew MAPLE. We can Help You

2. Will be to target Upgraders.
Headings could be;
The house too small, kids growing up. Need to find a bigger
Kids Growing Up, Need a Home with More Space?

Call Crew MAPLE, We can Help you

One the back can we have something about Crew Maple
Please do not forget to include contact numbers for Crew Maple Members

**We need to Incorporate Crew MAPLE logo, stock photos (not so American) to depict the people of the two cards, and our team photo.
for more info, please see profile pages for Tarin - http://qlbrenwick.com.au/about/our-team/profile.aspx?sid=4a1f9c3d-7b2e-4d81-a6c5-2e9f0b7d3a18&name=Tarin-Welbrook
Dulan - http://qlbrenwick.com.au/about/our-team/profile.aspx?sid=c93e2d71-0f5a-48b6-9e1c-7d4a8b26f053&name=Dulan-Merivale

We also have started using this description on our marketing products;
Crew MAPLE is a group of young enthusiastic individuals, living and breathing real estate 24/7. We love what we do and we do what we say. We work from our hearts, and our goal is to create a lasting presence, when we are not present. We hope you too will love experiencing the MAPLE difference.

```html
<!DOCTYPE html>
<html lang="en">
<head>
<meta charset="utf-8">
<title>Crew Maple – Give your Mower A Rest</title>
<link rel="stylesheet" href="https://fonts.googleapis.com/css2?family=Comic+Neue:wght@400;700&family=Patrick+Hand&family=Patrick+Hand+SC&display=swap">
<style>
  :root {
    --paper: #ffffff;
    --ink: #111111;
    --brand-red: #d9231d;
    --rule: #333333;
    --photo-top: #e9e9ea;
    --photo-mid: #8a8a8f;
    --photo-bottom: #1e1e22;
  }
  * { box-sizing: border-box; margin: 0; padding: 0; }
  html, body {
    width: 1200px;
    height: 2448px;
    overflow: hidden;
    background: var(--paper);
  }
  .leaflet {
    position: relative;
    width: 1200px;
    height: 2448px;
    background: var(--paper);
    color: var(--ink);
  }
  .brand {
    position: absolute;
    top: 90px;
    left: 130px;
    display: flex;
    align-items: center;
    gap: 34px;
  }
  .brand-dot {
    width: 70px;
    height: 70px;
    border-radius: 50%;
    background: var(--brand-red);
  }
  .brand-name {
    font-family: "Comic Neue", sans-serif;
    font-weight: 700;
    font-size: 150px;
    line-height: 1;
    color: var(--brand-red);
    letter-spacing: -2px;
  }
  .brand-rule {
    position: absolute;
    top: 325px;
    left: 158px;
    width: 892px;
    height: 3px;
    background: var(--rule);
  }
  .quote {
    position: absolute;
    top: 350px;
    left: 0;
    width: 100%;
    text-align: center;
    font-family: "Comic Neue", sans-serif;
    font-size: 54px;
    line-height: 82px;
  }
  .headline {
    position: absolute;
    top: 580px;
    left: 0;
    width: 100%;
    text-align: center;
    font-family: "Patrick Hand", cursive;
    font-size: 80px;
    line-height: 1;
  }
  .call {
    position: absolute;
    top: 735px;
    left: 0;
    width: 100%;
    text-align: center;
    font-family: "Patrick Hand", cursive;
    line-height: 1;
  }
  .call-line { display: block; font-size: 110px; }
  .call-sub { display: block; font-size: 90px; margin-top: 10px; }
  .about {
    position: absolute;
    top: 1030px;
    left: 188px;
    width: 836px;
    font-family: "Patrick Hand SC", cursive;
    font-size: 50px;
    line-height: 76px;
    text-align: justify;
    letter-spacing: 1px;
  }
  .team-photo {
    position: absolute;
    top: 1700px;
    left: 60px;
    width: 1130px;
    height: 748px;
    background: linear-gradient(to bottom, var(--photo-top) 0%, var(--photo-mid) 45%, var(--photo-bottom) 100%);
    border-radius: 300px 300px 0 0;
  }
</style>
</head>
<body>
  <main class="leaflet">
    <header class="brand">
      <span class="brand-dot"></span>
      <span class="brand-name">Crew Maple</span>
    </header>
    <div class="brand-rule"></div>

    <p class="quote">The yard is getting too big,<br>We cant look after the gardens any more.</p>

    <h1 class="headline">Give your Mower A Rest</h1>

    <h2 class="call">
      <span class="call-line">Call Crew MAPLE.</span>
      <span class="call-sub">We can Help You.</span>
    </h2>

    <p class="about">Crew MAPLE is a group of young enthusiastic individuals, living and breathing real estate 24/7. We love what we do and we do what we say. We work from our hearts, and our goal is to create a lasting presence, when we are not present. We hope you too will love experiencing the MAPLE difference.</p>

    <div class="team-photo" role="img" aria-label="Team photo: four Crew Maple agents in dark suits standing together, smiling"></div>
  </main>
</body>
</html>
```